Window and GutterCleaning Flyer A5 size double sided.

We need a double sided A5 flyer. Side 1, is for window cleaning, side 2 is for gutter cleaning. Licensed by Borough of Halvern Council.
Phone number 0800 315 4720.
Business address 7 Tarnlow Brae, North Pellin Edinburgh EH14 3RW.
www.clearpane-vista-services.com
We use a LoftPro Gutter inspection Cam to view your gutters first to see if they need doing.
Window cleaning ; Professional window cleaning services, what we offer, water fed pole window cleaning able to reach windows up to 60 feet.
Conservatory cleaning.
Conservatory roof cleaning.
Fascias & Soffits cleaning.
Excellent Customer Service.
Target Market(s)
domestic houses
Industry/Entity Type
window cleaning
Look and feel
Each slider illustrates characteristics of the customer's brand and the style your logo design should communicate.

```html
<!DOCTYPE html>
<html lang="en">
<head>
<meta charset="utf-8">
<title>Clearpane Vista Cleaning – A5 Flyer</title>
<link href="https://fonts.googleapis.com/css2?family=Barlow+Condensed:ital,wght@1,700&family=Poppins:wght@400;500;600;700&display=swap" rel="stylesheet">
<style>
:root{
  --navy:#1d3a66;
  --navy-deep:#152c52;
  --blue:#2f7cc4;
  --blue-bright:#4a9ee0;
  --pale:#dcebf8;
  --paper:#f3f6f9;
  --ink:#1f2f4a;
  --stage:#d6d4d1;
  --white:#ffffff;
}
*{box-sizing:border-box;margin:0;padding:0}
html,body{width:1200px;height:2503px;overflow:hidden;background:var(--stage);font-family:"Poppins",sans-serif;color:var(--ink)}
.flyer{position:absolute;left:180px;width:840px;height:1188px;background:var(--paper);overflow:hidden;box-shadow:0 6px 24px rgba(0,0,0,.12)}
.flyer--window{top:40px}
.flyer--gutter{top:1275px}
.hero-photo{position:absolute;left:0;top:0;width:840px;background:linear-gradient(120deg,var(--navy-deep) 0%,#3f6c9c 55%,#9fb9d2 100%)}
.title{position:absolute;font-family:"Barlow Condensed",sans-serif;font-style:italic;font-weight:700;color:var(--white);font-size:94px;line-height:.92;text-transform:uppercase;letter-spacing:1px}
.brand{position:absolute;right:40px;top:55px;display:flex;align-items:center;gap:8px;font-weight:700;font-size:30px;color:var(--navy)}
.brand__box{width:22px;height:22px;background:var(--navy)}
.band{position:absolute;left:0;width:840px}
.photo-circle{position:absolute;border-radius:50%;border:10px solid var(--white);box-shadow:0 4px 14px rgba(0,0,0,.25)}
.intro{position:absolute;color:var(--white);font-size:24px;line-height:40px;font-weight:400}
.section-title{position:absolute;font-weight:600;color:var(--navy);font-size:34px}
.body-copy{position:absolute;font-size:18.5px;line-height:30px;color:var(--ink)}
.reach{position:absolute;left:57px;top:895px;border-left:3px solid var(--navy);padding-left:10px}
.reach__small{font-size:14px;line-height:18px}
.reach__big{font-size:26px;font-weight:700;color:var(--navy)}
.phone-pill{position:absolute;left:57px;height:68px;width:410px;border-radius:34px;background:linear-gradient(90deg,var(--blue) 0%,var(--blue-bright) 100%);display:flex;align-items:center;color:var(--white);font-weight:600;font-size:34px}
.phone-pill__icon{width:72px;height:72px;margin-left:-2px;border-radius:50%;background:var(--white);border:5px solid var(--blue);display:flex;align-items:center;justify-content:center;margin-right:22px}
.licence{position:absolute;right:45px;font-size:13px;color:var(--ink)}
.footer{position:absolute;left:0;bottom:0;width:840px;height:88px;background:linear-gradient(90deg,var(--blue) 0%,var(--navy) 100%);display:flex;align-items:center;justify-content:space-around;color:var(--white);font-size:12px}
.footer__item{display:flex;align-items:center;gap:8px}
.footer__strip{position:absolute;left:0;bottom:88px;width:840px;height:14px;background:var(--pale)}
.lead{position:absolute;left:48px;top:345px;width:425px;color:var(--white);font-size:18px;font-weight:600;line-height:28px}
.lead__tag{background:var(--navy);padding:0 4px}
.lead__copy{margin-top:10px;font-size:11px;font-weight:400;line-height:17px;opacity:.92}
.services-head{position:absolute;left:48px;top:605px;width:744px;display:flex;align-items:center;gap:18px;font-weight:600;font-size:24px;color:var(--navy)}
.services-head__rule{flex:1;height:2px;background:var(--navy)}
.service{position:absolute;top:660px;width:200px;text-align:center}
.service__photo{width:100px;height:100px;border-radius:50%;margin:0 auto 14px}
.service__name{font-weight:600;font-size:13.5px;line-height:18px}
.service__desc{margin-top:10px;font-size:10.5px;line-height:15px}
.promise{position:absolute;left:0;top:880px;width:840px;height:150px;background:var(--pale);text-align:center;padding-top:22px}
.promise__title{margin-top:10px;font-weight:700;font-size:24px;color:var(--navy)}
.promise__line{margin-top:12px;font-size:12.5px}
</style>
</head>
<body>

<!-- Side 1 : window cleaning -->
<section class="flyer flyer--window">
  <div class="hero-photo" role="img" aria-label="Photo of a window cleaner wiping a large glass pane" style="height:380px"></div>
  <h1 class="title" style="left:50px;top:125px">Clearpane Window<br>Cleaning</h1>
  <div class="brand"><span class="brand__box"></span>CVS</div>
  <svg class="band" style="top:350px" width="840" height="220" viewBox="0 0 840 220">
    <polygon points="0,14 840,0 840,205 0,220" fill="var(--blue)"/>
    <polygon points="0,8 840,-6 840,4 0,18" fill="var(--white)"/>
  </svg>
  <p class="intro" style="left:52px;top:420px;width:430px">We offer a high-quality, professional window cleaning service across West Edinburgh.</p>
  <div class="photo-circle" role="img" aria-label="Photo of a cleaner using a water fed pole on a tall glass building" style="left:450px;top:268px;width:330px;height:330px;background:linear-gradient(160deg,#c9d8e6 0%,#7f9fbd 60%,#5b7898 100%)"></div>
  <h2 class="section-title" style="left:52px;top:598px">Window cleaning</h2>
  <p class="body-copy" style="left:52px;top:648px;width:740px">We offer a high quality, professional window cleaning service across west Edinburgh. Regular window cleaning helps to avoid the build-up of dirt and residue on the glass, meaning more light can get into your home or premises and can also improve its external appearance. We clean outside windows on houses and commercial buildings. In addition, we offer a conservatory cleaning service, gutter/rhone cleaning and painting, and builders cleans for those who have had work completed on their property.</p>
  <div class="reach">
    <p class="reach__small">Professional window cleaning services, what we offer, water<br>fed pole window cleaning able to reach windows</p>
    <p class="reach__big">up to 60 feet.</p>
  </div>
  <div class="phone-pill" style="top:1020px">
    <span class="phone-pill__icon"><svg width="32" height="32" viewBox="0 0 24 24"><path fill="var(--blue)" d="M6.6 10.8a15 15 0 0 0 6.6 6.6l2.2-2.2c.3-.3.7-.4 1-.2 1.1.4 2.3.6 3.6.6.6 0 1 .4 1 1V20c0 .6-.4 1-1 1A17 17 0 0 1 3 4c0-.6.4-1 1-1h3.5c.6 0 1 .4 1 1 0 1.3.2 2.5.6 3.6.1.3 0 .7-.2 1z"/></svg></span>0800 315 4720
  </div>
  <p class="licence" style="top:1062px">Licensed by Borough of Halvern Council</p>
  <div class="footer__strip"></div>
  <footer class="footer">
    <span class="footer__item"><svg width="14" height="14" viewBox="0 0 24 24"><path fill="#fff" d="M12 2a7 7 0 0 0-7 7c0 5 7 13 7 13s7-8 7-13a7 7 0 0 0-7-7zm0 9.5A2.5 2.5 0 1 1 12 6.5a2.5 2.5 0 0 1 0 5z"/></svg>7 Tarnlow Brae, North Pellin Edinburgh EH14 3RW</span>
    <span class="footer__item"><svg width="14" height="14" viewBox="0 0 24 24"><path fill="#fff" d="M3 5h18v14H3zm2 2v.5l7 4.5 7-4.5V7z"/></svg>info@clearpane-vista-services.com</span>
    <span class="footer__item"><svg width="14" height="14" viewBox="0 0 24 24"><circle cx="12" cy="12" r="9" fill="none" stroke="#fff" stroke-width="2"/><path d="M3 12h18M12 3c3 3 3 15 0 18M12 3c-3 3-3 15 0 18" fill="none" stroke="#fff" stroke-width="1.5"/></svg>www.clearpane-vista-services.com</span>
  </footer>
</section>

<!-- Side 2 : gutter cleaning -->
<section class="flyer flyer--gutter">
  <div class="hero-photo" role="img" aria-label="Photo of a gloved hand clearing a roof gutter" style="height:345px;background:linear-gradient(120deg,var(--navy-deep) 0%,#2f5786 50%,#6f8a6a 100%)"></div>
  <h1 class="title" style="left:50px;top:85px">Gutter<br><span style="padding-left:45px">Cleaning</span></h1>
  <svg class="band" style="top:325px" width="840" height="275" viewBox="0 0 840 275">
    <polygon points="0,10 840,0 840,262 0,272" fill="var(--blue)"/>
  </svg>
  <div class="photo-circle" role="img" aria-label="Photo of a worker in a respirator mask holding a gutter inspection camera" style="left:488px;top:300px;width:330px;height:330px;background:linear-gradient(150deg,#6b3a34 0%,#8a8d94 55%,#3f4f66 100%)"></div>
  <div class="lead">
    <p>We use a LoftPro Gutter<br><span class="lead__tag">INSPECTION CAM</span> to view<br>your gutters first to see if they need doing.</p>
    <p class="lead__copy">Gutters are an important part of your home, letting rain drain away from roofs and walls. When they are blocked, water can spill over, stain brickwork and cause damp inside. Leaves, moss and debris build up over time, so regular clearing keeps water moving and protects your property. We check every run with our camera, clear any blockage, flush the downpipes and leave the area tidy. A simple clean now can save a costly repair later on.</p>
  </div>
  <div class="services-head">Other Services<span class="services-head__rule"></span></div>
  <div class="service" style="left:92px">
    <div class="service__photo" role="img" aria-label="Photo of a clean conservatory roof" style="background:linear-gradient(140deg,#e8edf2,#8f9aa6)"></div>
    <p class="service__name">Conservatory<br>roof cleaning.</p>
    <p class="service__desc">We can clean the conservatory roof to remove the moss, algae, dirt and grime that has built up.</p>
  </div>
  <div class="service" style="left:320px">
    <div class="service__photo" role="img" aria-label="Photo of white fascias and soffits under a roof edge" style="background:linear-gradient(140deg,#6fae4f,#eef1f3)"></div>
    <p class="service__name">Fascias<br>&amp; Soffits cleaning.</p>
    <p class="service__desc">Our careful washing service is an affordable way to get your fascias looking bright and new again.</p>
  </div>
  <div class="service" style="left:548px">
    <div class="service__photo" role="img" aria-label="Photo of a cleaner washing a conservatory" style="background:linear-gradient(140deg,#3d6b3a,#a9b9c6)"></div>
    <p class="service__name">Conservatory<br>cleaning.</p>
    <p class="service__desc">We'll bring the shine back to your conservatory roof and windows, cleaning those hard-to-reach areas.</p>
  </div>
  <div class="promise">
    <svg width="34" height="26" viewBox="0 0 34 26"><path d="M4 22h26M8 22a9 9 0 0 1 18 0M17 5v4M9 8l2 3M25 8l-2 3" fill="none" stroke="var(--navy)" stroke-width="2" stroke-linecap="round"/></svg>
    <p class="promise__title">Excellent Customer Service</p>
    <p class="promise__line">All our services comes with a 100% satisfaction guarantee. If you're not happy, we'll come back and do it again for no additional cost.</p>
  </div>
  <div class="phone-pill" style="top:1042px;width:380px">
    <span class="phone-pill__icon"><svg width="32" height="32" viewBox="0 0 24 24"><path fill="var(--blue)" d="M6.6 10.8a15 15 0 0 0 6.6 6.6l2.2-2.2c.3-.3.7-.4 1-.2 1.1.4 2.3.6 3.6.6.6 0 1 .4 1 1V20c0 .6-.4 1-1 1A17 17 0 0 1 3 4c0-.6.4-1 1-1h3.5c.6 0 1 .4 1 1 0 1.3.2 2.5.6 3.6.1.3 0 .7-.2 1z"/></svg></span>0800 315 4720
  </div>
  <footer class="footer" style="height:70px">
    <span class="footer__item"><svg width="14" height="14" viewBox="0 0 24 24"><path fill="#fff" d="M12 2a7 7 0 0 0-7 7c0 5 7 13 7 13s7-8 7-13a7 7 0 0 0-7-7zm0 9.5A2.5 2.5 0 1 1 12 6.5a2.5 2.5 0 0 1 0 5z"/></svg>7 Tarnlow Brae, North Pellin Edinburgh EH14 3RW</span>
    <span class="footer__item"><svg width="14" height="14" viewBox="0 0 24 24"><path fill="#fff" d="M3 5h18v14H3zm2 2v.5l7 4.5 7-4.5V7z"/></svg>info@clearpane-vista-services.com</span>
    <span class="footer__item"><svg width="14" height="14" viewBox="0 0 24 24"><circle cx="12" cy="12" r="9" fill="none" stroke="#fff" stroke-width="2"/><path d="M3 12h18M12 3c3 3 3 15 0 18M12 3c-3 3-3 15 0 18" fill="none" stroke="#fff" stroke-width="1.5"/></svg>www.clearpane-vista-services.com</span>
  </footer>
</section>

</body>
</html>
```